Alloy wheel repair business needs a website

Install logo previously purchased from pixelbazaar, toolbar with dropdowns. services, gallery, clients , contact ect
Maybe mission statment

Target Market(s)

vehicle owners, auto dealers,insurance companies,

Industry/Entity Type

Alloy Wheel Repair

Coding

Coded - Design and coding required

Number of Pages Required

4 page

Font styles to use
Sans Serif

Colors
0054AA
0677BA
7BADD7
CADEEF
E8F1F8

```html
<!DOCTYPE html>
<html lang="en">
<head>
<meta charset="utf-8">
<title>Rimline Studio – Alloy Wheel Repair</title>
<link rel="stylesheet" href="https://fonts.googleapis.com/css2?family=Krona+One&family=Roboto:wght@400;500;700&display=swap">
<style>
:root{
  --navy:#0054AA;
  --blue:#0677BA;
  --btn:#3A86D0;
  --sky:#7BADD7;
  --ice:#CADEEF;
  --mist:#E8F1F8;
  --ink:#1b1b1b;
  --text:#444;
  --dark:#141414;
  --white:#fff;
}
*{box-sizing:border-box;margin:0;padding:0}
html,body{width:1200px;height:4270px;overflow:hidden}
body{position:relative;font-family:"Roboto",Arial,sans-serif;color:var(--text);background:var(--white)}
.abs{position:absolute}
.display{font-family:"Krona One","Arial Black",sans-serif;text-transform:uppercase}
.photo{position:absolute}
.btn{position:absolute;display:flex;align-items:center;justify-content:center;background:var(--btn);color:var(--white);font-family:"Krona One",sans-serif;font-size:15px;text-transform:uppercase;letter-spacing:1px}

/* top bar */
.topbar{left:0;top:0;width:1200px;height:45px;background:#000;color:var(--white);font-size:16px}
.topbar .contact-strip{position:absolute;left:555px;top:0;right:0;height:45px;background:var(--btn);clip-path:polygon(20px 0,100% 0,100% 100%,0 100%)}
.topbar span{position:absolute;top:13px;display:flex;align-items:center;gap:7px}

/* nav */
.nav{left:0;top:45px;width:1200px;height:87px;background:var(--white)}
.brand{position:absolute;display:flex;align-items:center;gap:10px;font-family:"Krona One",sans-serif;color:var(--btn);text-transform:uppercase;white-space:nowrap}
.brand .dot{width:22px;height:22px;border-radius:50%;background:var(--btn);flex:none}
.menu{position:absolute;left:423px;top:36px;display:flex;gap:44px;font-family:"Krona One",sans-serif;font-size:15px;color:var(--ink);text-transform:uppercase}
.menu .active{color:var(--btn)}

/* hero */
.hero{left:0;top:132px;width:1200px;height:620px;background:linear-gradient(90deg,#050505 0%,#1a1c22 40%,#3a4a66 70%,#2e5fa8 100%)}
.hero h1{position:absolute;left:128px;top:172px;font-size:52px;line-height:60px;color:var(--white);font-family:"Krona One",sans-serif;font-weight:400}
.hero p{position:absolute;left:128px;top:305px;width:400px;font-size:19px;line-height:24px;color:var(--white)}

/* headings with disc */
.sec-title{position:absolute;display:flex;align-items:center;gap:10px;font-size:36px;color:var(--ink);font-weight:400}
.sec-title .disc{width:40px;height:40px;border-radius:50%;background:#1d1d1d;border:4px solid var(--btn)}
.sec-title em{font-style:normal;color:var(--btn)}

/* mission */
.mission-text{left:585px;top:953px;width:470px;font-size:14.5px;line-height:18px;color:#333}

/* services */
.services{left:0;top:1342px;width:1200px;height:663px;background:var(--mist)}
.card{position:absolute;top:1510px;width:296px;height:401px;background:var(--white);box-shadow:0 2px 8px rgba(0,0,0,.08);text-align:center}
.card .photo{left:11px;top:15px;width:274px;height:185px}
.card h3{position:absolute;left:0;right:0;top:228px;font-size:20px;color:var(--ink);font-weight:400}
.card p{position:absolute;left:40px;right:40px;top:264px;font-size:14px;line-height:18px;color:#555}
.card .more{position:absolute;left:93px;top:337px;width:110px;height:36px;border:2px solid var(--btn);color:var(--btn);font-size:14px;display:flex;align-items:center;justify-content:center}
.arrow{position:absolute;top:1621px;width:22px;height:22px;border:2px solid #222;border-radius:50%}

/* why */
.why{left:0;top:2010px;width:1200px;height:477px;background:linear-gradient(120deg,#2F73C4 0%,#3B86D4 50%,#2F72C0 100%)}
.why h2{position:absolute;left:0;right:0;top:90px;text-align:center;font-size:34px;color:var(--white);font-weight:400}
.feature{position:absolute;top:167px;width:230px;text-align:center;color:var(--white)}
.feature .ring{margin:0 auto;width:110px;height:110px;border-radius:50%;background:var(--white);border:6px solid #1E5FA8;display:flex;align-items:center;justify-content:center}
.feature h4{margin-top:26px;font-size:17px;font-weight:700}
.feature p{margin-top:10px;font-size:14px;line-height:18px}

/* gallery */
.tile{position:absolute;width:304px;height:225px}

/* contact */
.contact{left:0;top:3331px;width:1200px;height:505px;background:linear-gradient(180deg,#1c1c1c 0%,#2b2b2b 50%,#151515 100%)}
.contact h2{position:absolute;left:0;right:0;top:82px;text-align:center;font-size:34px;color:var(--white);font-weight:400}
.contact p{position:absolute;left:260px;width:680px;top:146px;text-align:center;font-size:15px;line-height:19px;color:var(--white)}
.field{position:absolute;background:var(--white);font-size:14px;color:#333;padding:13px 12px}

/* footer */
.foot-h{position:absolute;font-family:"Krona One",sans-serif;font-size:17px;color:var(--ink);text-transform:uppercase;font-weight:400}
.foot-list{position:absolute;font-size:14px;line-height:26.5px;color:#444}
.social{position:absolute;top:4022px;width:20px;height:20px;border-radius:50%;background:#111}
.ci{position:absolute;left:825px;display:flex;gap:18px;font-size:14px;line-height:18px;color:#444}
.rule{left:124px;top:4197px;width:963px;height:1px;background:#cfcfcf}
.copy{left:0;right:0;top:4222px;text-align:center;font-size:14px;color:#333}
</style>
</head>
<body>

<header class="abs topbar">
  <span style="left:128px"><svg width="12" height="16" viewBox="0 0 12 16"><path d="M6 0a6 6 0 0 0-6 6c0 4.5 6 10 6 10s6-5.5 6-10a6 6 0 0 0-6-6zm0 8.5A2.5 2.5 0 1 1 6 3.5a2.5 2.5 0 0 1 0 5z" fill="#fff"/></svg>42 Foundry Lane, Millbrook PA 10000</span>
  <div class="contact-strip"></div>
  <span style="left:645px"><svg width="16" height="12" viewBox="0 0 16 12"><rect width="16" height="12" rx="1" fill="#fff"/><path d="M0 1l8 6 8-6" stroke="#3A86D0" stroke-width="1.5" fill="none"/></svg>hello@rimlinestudio.com</span>
  <span style="left:900px"><svg width="14" height="14" viewBox="0 0 24 24"><path d="M6.6 10.8a15 15 0 0 0 6.6 6.6l2.2-2.2a1 1 0 0 1 1-.25 11.4 11.4 0 0 0 3.6.57 1 1 0 0 1 1 1V20a1 1 0 0 1-1 1A17 17 0 0 1 3 4a1 1 0 0 1 1-1h3.5a1 1 0 0 1 1 1c0 1.25.2 2.45.57 3.6a1 1 0 0 1-.25 1z" fill="#fff"/></svg>Call: 555-014-2290</span>
</header>

<nav class="abs nav">
  <div class="brand" style="left:128px;top:30px;font-size:22px"><span class="dot"></span>Rimline Studio</div>
  <div class="menu">
    <span class="active">Home</span><span>Services ▾</span><span>Gallery</span><span>Clients</span><span>Contact</span>
  </div>
</nav>

<section class="abs hero" role="img" aria-label="Mechanic in blue overalls mounting a tyre on an alloy wheel in a workshop">
  <h1>RIMLINE<br>STUDIO</h1>
  <p>Lorem ipsum dolor sit amet, consectetur adipiscing elit, sed do eiusmod.</p>
  <div class="btn" style="left:128px;top:373px;width:202px;height:58px">Get a Quote</div>
</section>

<!-- mission -->
<div class="abs" style="left:447px;top:887px;width:74px;height:75px;border:2px solid var(--btn);border-left:none;border-bottom:none"></div>
<div class="photo" style="left:133px;top:852px;width:309px;height:335px;background:linear-gradient(135deg,#2a2a2a,#6b6f75 50%,#1e1e1e)" role="img" aria-label="Close-up of a car tyre on a silver alloy wheel"></div>
<div class="photo" style="left:293px;top:969px;width:254px;height:272px;background:linear-gradient(160deg,#9aa3ad,#4a5058 45%,#2b4f7e);border:4px solid #fff" role="img" aria-label="Mechanic tightening wheel nuts with an impact wrench"></div>
<h2 class="sec-title display" style="left:585px;top:900px;font-size:34px"><span class="disc"></span>Our <em>Mission</em></h2>
<p class="abs mission-text">Lorem ipsum dolor sit amet, consectetur adipiscing elit, sed do eiusmod tempor incididunt ut labore et dolore magna aliqua. Quis ipsum suspendisse ultrices gravida. Risus commodo viverra maec enas accumsan lacus vel facilisis. Lorem ipsum dolor sit amet, consectetur adipiscing elit, sed do eiusmod tempor incididunt ut lab ore et dolore magna aliqua. Quis ipsum suspendisse ultrices gravida. Risus commodo viverra maecenas accumsan lacus vel facilisisorem ipsum dolor sit amet, consectetur adipiscing elit, sed do eiusmod tempor incididunt ut labore et.</p>
<div class="btn" style="left:588px;top:1140px;width:156px;height:45px">About Us</div>

<!-- services -->
<section class="abs services"></section>
<h2 class="sec-title display" style="left:373px;top:1430px"><span class="disc"></span>Our <em>Services</em></h2>
<span class="arrow" style="left:77px"><svg width="18" height="18" viewBox="0 0 18 18"><path d="M13 9H5M8 6L5 9l3 3" stroke="#222" stroke-width="1.8" fill="none"/></svg></span>
<span class="arrow" style="left:1100px"><svg width="18" height="18" viewBox="0 0 18 18"><path d="M5 9h8M10 6l3 3-3 3" stroke="#222" stroke-width="1.8" fill="none"/></svg></span>
<article class="card" style="left:128px">
  <div class="photo" style="background:linear-gradient(135deg,#1f4f96,#d08a3a 55%,#2a2a2a)" role="img" aria-label="Technician repairing a wheel with sparks in the workshop"></div>
  <h3 class="display">Repairs</h3>
  <p>Lorem ipsum dolor sit amet, consectetur adipiscing elit, sed do eiusmod tempor incina.</p>
  <div class="more">Read More</div>
</article>
<article class="card" style="left:451px">
  <div class="photo" style="background:linear-gradient(135deg,#3a3a3a,#c9ccd0 50%,#6d7177)" role="img" aria-label="Silver alloy wheel being refinished"></div>
  <h3 class="display">Refinish</h3>
  <p>Lorem ipsum dolor sit amet, consectetur adipiscing elit, sed do eiusmod tempor incina.</p>
  <div class="more">Read More</div>
</article>
<article class="card" style="left:775px">
  <div class="photo" style="background:linear-gradient(135deg,#1d1d1d,#8a8f96 50%,#d9b27a)" role="img" aria-label="New tyre on an alloy wheel in a tyre shop"></div>
  <h3 class="display">Flare Kits</h3>
  <p>Lorem ipsum dolor sit amet, consectetur adipiscing elit, sed do eiusmod tempor incina.</p>
  <div class="more">Read More</div>
</article>

<!-- why choose us -->
<section class="abs why" role="img" aria-label="Blue toned wheel background">
  <h2 class="display">Why Choose Us?</h2>
  <div class="feature" style="left:105px">
    <div class="ring"><svg width="54" height="54" viewBox="0 0 54 54" fill="none" stroke="#3A86D0" stroke-width="2"><circle cx="27" cy="27" r="22"/><circle cx="27" cy="27" r="17"/><path d="M27 15v12l8 5"/></svg></div>
    <h4>Consectetulore</h4><p>Lorem ipsum dolor saet consectetur adipiscingtsed do eiusmod tempornc.</p>
  </div>
  <div class="feature" style="left:357px">
    <div class="ring"><svg width="54" height="54" viewBox="0 0 54 54" fill="none" stroke="#3A86D0" stroke-width="2"><rect x="8" y="16" width="38" height="22" rx="2" transform="rotate(-20 27 27)"/><circle cx="27" cy="27" r="8"/><path d="M27 22v10M24 25h5a2 2 0 0 1 0 4h-4"/></svg></div>
    <h4>Consectetulore</h4><p>Lorem ipsum dolor saet consectetur adipiscingtsed do eiusmod tempornc.</p>
  </div>
  <div class="feature" style="left:609px">
    <div class="ring"><svg width="54" height="54" viewBox="0 0 54 54" fill="none" stroke="#3A86D0" stroke-width="2"><circle cx="27" cy="27" r="8"/><path d="M27 9v6M27 39v6M9 27h6M39 27h6M14 14l4 4M36 36l4 4M14 40l4-4M36 18l4-4"/><circle cx="27" cy="27" r="14"/></svg></div>
    <h4>Consectetulore</h4><p>Lorem ipsum dolor saet consectetur adipiscingtsed do eiusmod tempornc.</p>
  </div>
  <div class="feature" style="left:859px">
    <div class="ring"><svg width="54" height="54" viewBox="0 0 54 54" fill="none" stroke="#3A86D0" stroke-width="2"><circle cx="27" cy="23" r="15"/><path d="M20 23l5 5 9-10M19 35l-4 12 7-3 5 5 2-10M35 35l4 12-7-3"/></svg></div>
    <h4>Consectetulore</h4><p>Lorem ipsum dolor saet consectetur adipiscingtsed do eiusmod tempornc.</p>
  </div>
</section>

<!-- gallery -->
<h2 class="sec-title display" style="left:440px;top:2605px"><span class="disc"></span>Gallery</h2>
<div class="tile" style="left:128px;top:2678px;background:linear-gradient(135deg,#1e2b3a,#9da4ac 50%,#2b5c9c)" role="img" aria-label="Hands fitting wheel bolts to an alloy wheel"></div>
<div class="tile" style="left:447px;top:2678px;background:linear-gradient(135deg,#202020,#a82424 45%,#9a9ea4)" role="img" aria-label="Alloy wheel with red brake caliper"></div>
<div class="tile" style="left:767px;top:2678px;background:linear-gradient(135deg,#3b3935,#6e6a63 50%,#1f1e1c)" role="img" aria-label="Wheel being balanced on a machine"></div>
<div class="tile" style="left:128px;top:2921px;background:linear-gradient(135deg,#e8b070,#4d4d4d 45%,#1a1a1a)" role="img" aria-label="Row of new tyres in warm light"></div>
<div class="tile" style="left:447px;top:2921px;background:linear-gradient(135deg,#2a2a2a,#5a6b84 55%,#8a4b36)" role="img" aria-label="Mechanic inspecting a tyre in a workshop"></div>
<div class="tile" style="left:767px;top:2921px;background:linear-gradient(135deg,#c8ccd2,#50555c 50%,#1d1d1d)" role="img" aria-label="Mechanic changing a car wheel"></div>
<div class="btn" style="left:522px;top:3195px;width:156px;height:45px">View More</div>

<!-- contact -->
<section class="abs contact" role="img" aria-label="Dark background of stacked tyres">
  <h2 class="display">Contact Us</h2>
  <p>Lorem ipsum dolor sit amet, consectetur adipiscing elit, sed do eiusmod tempor incididunt ut labore et dolore magna aliqua. Quis ipsum suspendisse ultrices gravis commodo</p>
  <div class="field" style="left:227px;top:212px;width:230px;height:48px">Name:</div>
  <div class="field" style="left:464px;top:212px;width:253px;height:48px">Email:</div>
  <div class="field" style="left:726px;top:212px;width:243px;height:48px">Phone:</div>
  <div class="field" style="left:227px;top:267px;width:742px;height:127px;padding:13px 20px">Message:</div>
  <div class="btn" style="left:537px;top:372px;width:126px;height:44px">Submit</div>
</section>

<!-- footer -->
<footer>
  <div class="brand" style="left:149px;top:3930px;font-size:14px"><span class="dot" style="width:18px;height:18px"></span>Rimline Studio</div>
  <span class="social" style="left:180px"></span><span class="social" style="left:222px"></span><span class="social" style="left:262px"></span>

  <h5 class="foot-h" style="left:398px;top:3936px;font-size:15px">Home</h5>
  <div class="foot-list" style="left:398px;top:3963px">About<br>Services<br>Pricing<br>Gallery<br>Contact</div>

  <h5 class="foot-h" style="left:545px;top:3932px">Hours</h5>
  <div class="foot-list" style="left:545px;top:3963px">Mon<br>Tue<br>Wed<br>Thu<br>Friday<br>Saturday<br>Sunday</div>
  <div class="foot-list" style="left:630px;top:3963px">7:00am - 5:00pm<br>7:00am - 5:00pm<br>7:00am - 5:00pm<br>7:00am - 5:00pm<br>7:00am - 4:00pm<br>7:00am - 12:00pm<br>Closed</div>

  <h5 class="foot-h" style="left:825px;top:3932px">Contact Us</h5>
  <div class="ci" style="top:3972px"><svg width="22" height="22" viewBox="0 0 24 24"><path d="M6.6 10.8a15 15 0 0 0 6.6 6.6l2.2-2.2a1 1 0 0 1 1-.25 11.4 11.4 0 0 0 3.6.57 1 1 0 0 1 1 1V20a1 1 0 0 1-1 1A17 17 0 0 1 3 4a1 1 0 0 1 1-1h3.5a1 1 0 0 1 1 1c0 1.25.2 2.45.57 3.6a1 1 0 0 1-.25 1z" fill="#3A86D0"/></svg><span style="padding-left:2px">Call Us:<br>555-014-2290</span></div>
  <div class="ci" style="top:4036px"><svg width="22" height="18" viewBox="0 0 22 18"><rect width="22" height="16" y="1" rx="2" fill="#3A86D0"/><path d="M1 3l10 7 10-7" stroke="#fff" stroke-width="1.6" fill="none"/></svg><span style="padding-left:2px">Email:<br>hello@rimlinestudio.com</span></div>
  <div class="ci" style="top:4107px"><svg width="22" height="26" viewBox="0 0 12 16"><path d="M6 0a6 6 0 0 0-6 6c0 4.5 6 10 6 10s6-5.5 6-10a6 6 0 0 0-6-6z" fill="#3A86D0"/><circle cx="6" cy="6" r="2.3" fill="#fff"/></svg><span style="padding-left:2px">Address: 42 Foundry Lane<br>Millbrook PA 10000</span></div>

  <span class="abs" style="left:82px;top:4176px;width:38px;height:38px;border-radius:50%;background:#1d1d1d;border:4px solid var(--btn)"></span>
  <div class="abs rule"></div>
  <p class="abs copy">Copyright 2023 All rights are reserved.</p>
</footer>

</body>
</html>
```